Tarvimo Software (a new software house) needs a Wordpress web site

We need a Wordpress web site. We develop innovative software as a service (on demand) for companies and cunsumers.
Updates

Project Deadline Extended
Reason: I need extra days to analyze.

Target Market(s)

Consumers who use mobile software to access useful information about your day by day in a crowd plataform and on demand.

Industry/Entity Type

Software

Requirements
Must have
• See wordpress template suggestion:
http://themes.plondavi.com/?theme=marbleton

```html
<!DOCTYPE html>
<html lang="en">
<head>
<meta charset="utf-8">
<title>Tarvimo Software</title>
<link href="https://fonts.googleapis.com/css2?family=Arimo:wght@400;700&family=Play:wght@400;700&display=swap" rel="stylesheet">
<style>
:root{
  --ink:#222;
  --text:#555;
  --muted:#777;
  --accent:#5a6fc0;
  --nav-top:#9aabdf;
  --nav-bottom:#7286c6;
  --nav-active:#333;
  --circle:#a6b2de;
  --circle-light:#e9ecf7;
  --frame:#d6d6d6;
  --bar:#f2f2f2;
  --footer:#3b3b3b;
  --footer-text:#e4e4e4;
  --button:#1e6dc4;
}
*{box-sizing:border-box;margin:0;padding:0}
html,body{width:1010px;height:1200px;overflow:hidden;background:#fff}
body{position:relative;font-family:"Arimo",Arial,sans-serif;color:var(--text);font-size:12px}
.abs{position:absolute}
.heading{font-family:"Play",sans-serif;font-weight:400;color:var(--accent)}

/* header */
.brand{left:76px;top:22px;display:flex;align-items:center;gap:12px}
.brand-dot{width:40px;height:40px;border-radius:50%;background:var(--ink)}
.brand-name{font-size:26px;font-weight:700;color:var(--ink);letter-spacing:-.3px}
.search{left:609px;top:34px;width:175px;height:24px;border:1px solid #ccc;background:#fafafa;font-size:11px;color:#444;padding:5px 10px}
.search svg{position:absolute;right:8px;top:5px}
.register{left:785px;top:34px;width:72px;height:24px;background:var(--button);color:#fff;font-size:11px;padding:6px 0 0 26px}
.register svg{position:absolute;left:10px;top:6px}
.login{left:857px;top:34px;width:78px;height:24px;border:1px solid #ccc;background:#f6f6f6;font-size:11px;color:#333;padding:5px 0 0 24px}
.login svg{position:absolute;left:9px;top:6px}

/* nav */
.nav{left:0;top:90px;width:1010px;height:46px;background:linear-gradient(var(--nav-top),var(--nav-bottom));border-top:1px solid #c5cde8}
.nav-item{position:absolute;top:0;height:45px;line-height:45px;text-align:center;color:#fff;font-weight:700;font-size:12px;text-transform:uppercase;border-right:1px solid #8596cf}
.nav-item.active{background:var(--nav-active)}

/* hero */
.hero{left:0;top:136px;width:1010px;height:305px;background:linear-gradient(100deg,#f4f4f4 0%,#e9e9e9 55%,#d6d6d6 100%)}
.hero-lead{left:107px;top:64px;font-size:24px;color:#333}
.hero-title{left:107px;top:93px;font-size:31.5px}
.hero-text{left:106px;top:136px;width:350px;font-size:11.4px;line-height:19.3px;color:#555}
.dot{top:255px;width:12px;height:12px;border-radius:50%;background:#888}
.dot.current{background:#fff;border:2px solid #777;box-shadow:0 0 0 2px #ddd}
.hero-art{left:560px;top:25px;width:330px;height:270px;border-radius:20px;background:radial-gradient(circle at 60% 55%,#8a8f9a,#cfd3dc 60%,rgba(220,220,220,0))}

/* downloads */
.dl-title{left:78px;top:470px;font-size:23px}
.dl-text{left:78px;top:504px;width:392px;font-size:11.4px;line-height:19.3px}
.device{top:464px;width:104px;height:104px;border-radius:50%;background:var(--circle)}
.device svg{position:absolute;left:0;top:0}
.device.current{background:var(--circle-light)}
.device-label{position:absolute;width:100%;top:34px;text-align:center;font-weight:700;font-size:15px;color:#333;line-height:19px}
.rule{left:76px;top:601px;width:860px;height:1px;background:#e3e3e3}

/* columns */
.col-title{font-size:23px;top:626px}
.what-box{left:77px;top:668px;width:582px;height:184px;border:3px solid var(--frame);background:linear-gradient(90deg,#fbfbfb 0%,#f2f2f2 55%,#e8e8e8 100%)}
.what-photo{position:absolute;right:0;top:0;width:230px;height:178px;background:linear-gradient(120deg,#e6e6e6,#6b6f74 45%,#b38a72 80%,#d9c2b0)}
.what-head{position:absolute;left:16px;top:20px;font-size:13px;color:var(--ink)}
.what-text{position:absolute;left:16px;top:48px;width:296px;font-size:11.4px;line-height:19.3px;text-align:justify}
.thumb{top:915px;width:185px;height:100px;border:3px solid var(--frame)}
.thumb-a{left:78px;background:radial-gradient(circle at 50% 45%,#9aa0a8,#3a3c40 75%)}
.thumb-b{left:276px;background:#444;color:#fff;font-size:12px;line-height:18px;padding:14px 8px 0 12px;white-space:nowrap}
.thumb-c{left:473px;background:radial-gradient(circle at 50% 45%,#d9dde6,#f7f7f7 70%)}
.app-btn{position:absolute;left:12px;top:60px;width:158px;height:26px;border-radius:2px;background:linear-gradient(#9a9a9a,#707070);border:1px solid #aaa;text-align:center;line-height:24px;font-weight:700;font-size:12.5px;color:#fff}
.more{top:1029px;height:31px;background:linear-gradient(#f8f8f8,#ececec);border:1px solid #ddd;color:var(--muted);font-size:12px;line-height:29px;padding-left:12px}
.more svg{position:absolute;right:10px;top:9px}

/* blog */
.blog-photo{left:682px;top:668px;width:254px;height:122px;border:3px solid var(--frame);background:linear-gradient(135deg,#1c1c1c,#5b5e63 45%,#c8c8c8 60%,#2a2a2a)}
.blog-title{left:694px;top:804px;font-size:14px;color:var(--ink)}
.blog-meta{left:694px;top:825px;font-size:11px;font-style:italic;color:var(--muted);word-spacing:2px}
.blog-text{left:694px;top:847px;width:230px;font-size:11.4px;line-height:19.3px;text-align:justify}
.share{top:997px;height:16px;display:flex;gap:3px;font-size:10px;color:#333}
.share span{border:1px solid #ccc;border-radius:2px;padding:1px 5px;background:#f6f6f6;line-height:12px}

/* footer */
.footer{left:0;top:1084px;width:1010px;height:116px;background:var(--footer)}
.footer-links{left:76px;top:1104px;font-size:12px;color:var(--footer-text);word-spacing:1px}
.footer-links b{font-weight:400;margin:0 7px}
.copyright{left:76px;top:1132px;font-size:12px;color:var(--footer-text)}
.social{top:1162px;width:20px;height:20px;border-radius:3px}
.store{top:1107px;height:34px;border-radius:4px}
</style>
</head>
<body>

<header>
  <div class="abs brand"><span class="brand-dot"></span><span class="brand-name">Tarvimo Software</span></div>
  <div class="abs search">Search
    <svg width="14" height="14" viewBox="0 0 14 14"><circle cx="5.5" cy="5.5" r="4" fill="none" stroke="#333" stroke-width="2"/><line x1="8.5" y1="8.5" x2="13" y2="13" stroke="#333" stroke-width="2.5"/></svg>
  </div>
  <div class="abs register">
    <svg width="10" height="12" viewBox="0 0 10 12"><path d="M2 5V3.5a3 3 0 0 1 6 0V5" fill="none" stroke="#fff" stroke-width="1.6"/><rect x="0.5" y="5" width="9" height="7" fill="#fff"/></svg>Regsiter
  </div>
  <div class="abs login">
    <svg width="11" height="11" viewBox="0 0 11 11"><circle cx="5.5" cy="3" r="2.7" fill="#555"/><path d="M0 11c0-4 11-4 11 0z" fill="#555"/></svg>Log in
    <svg style="left:60px;top:9px" width="8" height="5" viewBox="0 0 8 5"><path d="M0 0h8L4 5z" fill="#444"/></svg>
  </div>
</header>

<nav class="abs nav">
  <div class="nav-item active" style="left:79px;width:86px">Home</div>
  <div class="nav-item" style="left:165px;width:116px">About us</div>
  <div class="nav-item" style="left:281px;width:143px">Our services</div>
  <div class="nav-item" style="left:424px;width:155px">Our softwares</div>
  <div class="nav-item" style="left:579px;width:112px">Our blog</div>
  <div class="nav-item" style="left:691px;width:130px">Contact us</div>
  <div class="nav-item" style="left:821px;width:112px">Support</div>
</nav>

<section class="abs hero">
  <div class="abs heading hero-lead" style="color:#333">We develop innovative</div>
  <div class="abs heading hero-title">software as a service</div>
  <p class="abs hero-text">Fusce euismod, orci at accumsan consectetur, elit magna ornare nulla, nec rutrum velit eros vel mauris. Etiam leo elit, laoreet vel justo ac, dignissim rhoncus ipsum. Duis sed justo diam.</p>
  <span class="abs dot current" style="left:111px"></span>
  <span class="abs dot" style="left:138px"></span>
  <span class="abs dot" style="left:164px"></span>
  <span class="abs dot" style="left:191px"></span>
  <div class="abs hero-art" role="img" aria-label="Smartphone with colourful app icons floating around it"></div>
</section>

<section>
  <h2 class="abs heading dl-title">Download softwares&nbsp; for...</h2>
  <p class="abs dl-text">Curabitur at enim quis diam tempor suscipit. Curabitur viverra placerat nibh, at semper urna blandit at. Vestibulum placerat nisl eu sem iaculis dapibus. Nam accumsan nisl ultrices mattis fringilla.</p>
  <div class="abs device current" style="left:484px">
    <svg width="104" height="104" viewBox="0 0 104 104"><rect x="36" y="25" width="32" height="56" rx="3" fill="none" stroke="#fff" stroke-width="3"/></svg>
    <div class="device-label">For<br>Mobiels</div>
  </div>
  <div class="abs device" style="left:598px">
    <svg width="104" height="104" viewBox="0 0 104 104"><rect x="30" y="20" width="44" height="64" rx="4" fill="none" stroke="#fff" stroke-width="3"/><rect x="36" y="28" width="32" height="44" fill="none" stroke="#fff" stroke-width="2"/><circle cx="52" cy="78" r="2.5" fill="#fff"/></svg>
  </div>
  <div class="abs device" style="left:714px">
    <svg width="104" height="104" viewBox="0 0 104 104"><rect x="27" y="30" width="50" height="36" rx="2" fill="none" stroke="#fff" stroke-width="3"/><path d="M20 70h64l-4 6H24z" fill="none" stroke="#fff" stroke-width="3"/></svg>
  </div>
  <div class="abs device" style="left:830px">
    <svg width="104" height="104" viewBox="0 0 104 104"><rect x="18" y="24" width="68" height="48" rx="5" fill="none" stroke="#fff" stroke-width="3"/><rect x="37" y="76" width="30" height="8" rx="4" fill="none" stroke="#fff" stroke-width="3"/></svg>
  </div>
  <div class="abs rule"></div>
</section>

<main>
  <h2 class="abs heading col-title" style="left:78px">What we do</h2>
  <div class="abs what-box">
    <div class="what-photo" role="img" aria-label="Hand holding a smartphone showing its home screen"></div>
    <h3 class="what-head" style="font-weight:400">Etiam eu vulputate velit, tempor lectus.</h3>
    <p class="what-text">Sed tristique, purus et ornare volutpat, justo ipsum laoreet lacus, sit amet laoreet purus sapien vel leo. Nunc ac venenatis nisl. Fusce pharetra nisl metus, sit amet consect-etur urna lacinia ac. Proin quam metus, pretium eu dui eu, vulputate mattis nibh. Duis feugiat, sem ut dignissim elementum sodales pellentesque.</p>
  </div>

  <h2 class="abs heading col-title" style="left:78px;top:873px">What we did</h2>
  <div class="abs thumb thumb-a" role="img" aria-label="Smartphone with colourful cables on a dark background"></div>
  <div class="abs thumb thumb-b">Duis feugiat, sem ut dignissim<br>elementum sodales
    <div class="app-btn">View this Application</div>
  </div>
  <div class="abs thumb thumb-c" role="img" aria-label="Box filled with colourful app icons"></div>
  <div class="abs more" style="left:77px;width:582px">View all Posts
    <svg width="10" height="12" viewBox="0 0 10 12"><path d="M2 1l5 5-5 5" fill="none" stroke="#888" stroke-width="2.5"/></svg>
  </div>

  <h2 class="abs heading col-title" style="left:683px">Our Blog</h2>
  <div class="abs blog-photo" role="img" aria-label="Hands typing on a tablet screen"></div>
  <h3 class="abs blog-title" style="font-weight:400">Morbi neque orci, suscipit</h3>
  <div class="abs blog-meta">June-25-2013&nbsp; / &nbsp;10.15 a.m&nbsp; / &nbsp;by John</div>
  <p class="abs blog-text">Aliquam vel congue purus. Maecenas ut auctor lorem, quis aliquam quam. Aliquam erat volutpat. Maecenas id ante scelerisque, suscipit magna ac, mollis neque. Vestibulum ac fermentum risus. Donec iaculis sit amet libero vel rutrum. Vestibulum auctor nulla urna, in pretium enim hendreri.</p>
  <div class="abs share" style="left:694px"><span>Share</span><span>3k</span></div>
  <div class="abs share" style="left:762px"><span>Post</span><span>316</span></div>
  <div class="abs share" style="left:838px"><span>Plus</span><span>81</span></div>
  <div class="abs more" style="left:682px;width:254px">View all Posts
    <svg width="10" height="12" viewBox="0 0 10 12"><path d="M2 1l5 5-5 5" fill="none" stroke="#888" stroke-width="2.5"/></svg>
  </div>
</main>

<footer class="abs footer"></footer>
<div class="abs footer-links">Home<b>|</b>About us<b>|</b>Our Services<b>|</b>Our Softwares<b>|</b>Our Blog<b>|</b>Contact us<b>|</b>Support</div>
<div class="abs copyright">Copyright&nbsp; ©&nbsp; 2013&nbsp;&nbsp;&nbsp; Tarvimo software.&nbsp;&nbsp; All rights reserved.</div>
<span class="abs social" style="left:76px;background:#4a66a8"></span>
<span class="abs social" style="left:102px;background:#44b4e8"></span>
<span class="abs store" style="left:742px;width:103px;background:#6b6b6b;border:1px solid #888"></span>
<span class="abs store" style="left:853px;width:81px;background:#111;border:1px solid #555"></span>

</body>
</html>
```